Online-Marketing Material
wir sind sehr zufrieden mit allem. danke
Zielgruppe
Wir vertreiben auf unserer Plattform morvelhaus17.de diverse Produkte rund um das Thema Kaffee. Unsere Zielgruppe sind Kaffeeliebhaber von jung bis alt.
Aufgabenstellung
Für unsere neue Domain brulino.at benötigen wir diverse Grafiken / Banner für die verschiedenen Bereiche unseres Shops. Momentan gibt es eine Staging Site um sich einen Überblick zu verschaffen.
Auftrag hier ist ein Startseitenbanner in der Größe 3200x1240 unter Berücksichtigung der aktuellen Farben in unserem Shop, der Thematik Kaffee und mehr und dem dazugehörigen neuen bereits entworfenem Logo.
Info Testseite: http://www.brulino.at/_staging/ Login mit admin und velo#482
Gerne kann eigenes Bildmaterial geliefert werden

```html
<!DOCTYPE html>
<html lang="de">
<head>
<meta charset="utf-8">
<title>brulino.at – Kaffee und mehr</title>
<link rel="stylesheet" href="https://fonts.googleapis.com/css2?family=Poppins:wght@400;500;700&family=Pacifico&display=swap">
<style>
  :root {
    --brand-red: #a42b2a;
    --ink: #1e1a18;
    --logo-brown: #3b2a23;
    --line: #2a2a2a;
    --muted: #8a8a8a;
    --paper: #ffffff;
    --hero-dark: #4a2e1f;
    --hero-mid: #8c6a4c;
    --hero-light: #c9ad88;
  }
  * { box-sizing: border-box; margin: 0; padding: 0; }
  html, body { width: 1200px; height: 645px; overflow: hidden; background: var(--paper); }
  body { position: relative; font-family: "Poppins", sans-serif; color: var(--ink); }

  .promo-bar {
    position: absolute; left: 0; top: 0; width: 1200px; height: 22px;
    background: var(--brand-red); color: #fff;
    font-size: 9px; line-height: 22px; text-align: center; letter-spacing: .1px;
  }

  .search {
    position: absolute; left: 99px; top: 65px; width: 219px; height: 20px;
    border: 1px solid var(--line); border-radius: 10px;
    font-size: 8px; color: var(--muted); line-height: 18px; padding-left: 6px;
  }
  .search svg { position: absolute; right: 6px; top: 3px; }

  .logo {
    position: absolute; left: 500px; top: 40px; width: 200px; text-align: center;
  }
  .logo-mark {
    display: block; width: 46px; height: 46px; margin: 0 auto 8px;
    border-radius: 50%; background: var(--logo-brown);
  }
  .logo-name {
    font-weight: 700; font-size: 22px; line-height: 24px; color: var(--logo-brown);
  }

  .account {
    position: absolute; left: 978px; top: 64px; display: flex; align-items: center; gap: 9px;
  }
  .cart { position: relative; }
  .cart-count {
    position: absolute; left: 11px; top: -5px; width: 11px; height: 11px; border-radius: 50%;
    background: var(--brand-red); color: #fff; font-size: 7px; line-height: 11px; text-align: center;
  }
  .cart-total { font-size: 10px; margin-left: -3px; }
  .cart-total sup { font-size: 6px; }

  .main-nav {
    position: absolute; left: 0; top: 135px; width: 1200px;
    display: flex; justify-content: center; gap: 18px;
    font-size: 11px; font-weight: 500; letter-spacing: .1px; text-transform: uppercase;
  }

  .hero {
    position: absolute; left: 99px; top: 168px; width: 1012px; height: 392px;
    background:
      radial-gradient(ellipse 18% 30% at 52% 25%, #e9e2d6 0%, #d8c9b0 60%, transparent 100%),
      linear-gradient(100deg, var(--hero-light) 0%, var(--hero-mid) 30%, var(--hero-dark) 55%, var(--hero-mid) 78%, var(--hero-dark) 100%);
    overflow: hidden;
  }
  .hero-title {
    position: absolute; left: 0; top: 118px; width: 100%; text-align: center;
    font-family: "Pacifico", cursive; font-size: 90px; line-height: 130px; color: #fff;
  }

  .brand-strip {
    position: absolute; left: 99px; top: 574px; width: 1002px; height: 62px;
  }
  .strip-arrow {
    position: absolute; top: 11px; width: 19px; height: 38px;
    border: 1px solid var(--line); display: flex; align-items: center; justify-content: center;
  }
  .strip-arrow.prev { left: 0; border-left: none; }
  .strip-arrow.next { right: 0; border-right: none; }
  .brand {
    position: absolute; top: 0; height: 62px; width: 140px; margin-left: -70px;
    display: flex; align-items: center; justify-content: center; gap: 5px;
    font-size: 13px; font-weight: 500; color: var(--muted); white-space: nowrap;
  }
  .brand-dot { width: 30px; height: 30px; border-radius: 50%; background: #a9a9a9; }
</style>
</head>
<body>
  <div class="promo-bar">Frische Garantie - Beste Markenqualität - Lieferung in 1-3 Werktagen</div>

  <div class="search">Suchbegriff eingeben...
    <svg width="13" height="13" viewBox="0 0 13 13" fill="none" stroke="#1e1a18" stroke-width="1.5"><circle cx="5.5" cy="5.5" r="4.3"/><line x1="8.6" y1="8.6" x2="12" y2="12"/></svg>
  </div>

  <div class="logo">
    <span class="logo-mark"></span>
    <div class="logo-name">brulino.at</div>
  </div>

  <div class="account">
    <svg width="18" height="16" viewBox="0 0 18 16" fill="none" stroke="#1e1a18" stroke-width="1.4"><path d="M9 15 L2.2 8.2 A3.9 3.9 0 0 1 9 3 A3.9 3.9 0 0 1 15.8 8.2 Z"/></svg>
    <svg width="16" height="17" viewBox="0 0 16 17" fill="none" stroke="#1e1a18" stroke-width="1.4"><circle cx="8" cy="5" r="3.6"/><path d="M1.5 16.5 Q1.5 10 8 10 Q14.5 10 14.5 16.5"/></svg>
    <span class="cart">
      <svg width="18" height="17" viewBox="0 0 18 17" fill="none" stroke="#1e1a18" stroke-width="1.4"><rect x="1.5" y="5" width="15" height="11" rx="1.5"/><path d="M6 7 V3.5 A3 3 0 0 1 12 3.5 V7"/></svg>
      <span class="cart-count">0</span>
    </span>
    <span class="cart-total">0,<sup>00*</sup></span>
  </div>

  <nav class="main-nav">
    <span>Kaffee &amp; Espresso</span>
    <span>Pure Tee - Kalvoro</span>
    <span>Kaffeekapseln</span>
    <span>Kaffeepads</span>
    <span>Büro Kaffee Service</span>
    <span>Probierpakete</span>
    <span>Angebote &amp; Neu</span>
  </nav>

  <section class="hero" role="img" aria-label="Foto: Kaffeetasse mit Crema, Kaffeebohnen, Jutesack mit Blättern, Zimtstangen, Löffel mit gemahlenem Kaffee und Kaffeemühle">
    <h1 class="hero-title">Kaffee und mehr</h1>
  </section>

  <div class="brand-strip">
    <span class="strip-arrow prev"><svg width="8" height="14" viewBox="0 0 8 14" fill="none" stroke="#1e1a18" stroke-width="1.2"><polyline points="7,1 1,7 7,13"/></svg></span>
    <span class="brand" style="left:94px">Varelli</span>
    <span class="brand" style="left:256px">Miravista</span>
    <span class="brand" style="left:419px"><span class="brand-dot"></span>Orvanta</span>
    <span class="brand" style="left:583px">Caffè Dorano</span>
    <span class="brand" style="left:744px">Tessaro</span>
    <span class="brand" style="left:907px">Caffè Lunetti</span>
    <span class="strip-arrow next"><svg width="8" height="14" viewBox="0 0 8 14" fill="none" stroke="#1e1a18" stroke-width="1.2"><polyline points="1,1 7,7 1,13"/></svg></span>
  </div>
</body>
</html>
```